Patty Cove Business Card/Logo/Stationary (Restaurant)

Please check out our instagram (@pattycove) for inspiration.

This project is for a NEW design... examples below are just for reference. Please do not submit the images below on a card.

We're a New Zealand inspired gastropub serving award-winning gourmet burgers. Our restaurant is called Patty Cove! A Bach is a New Zealand term for a ‘holiday home’ where family and friends choose to vacation. Baches are an extensive part of New Zealand’s culture and were thought to be originally short for bachelor pad, but actually tended to be a family holiday home.

We've had the same bland business card design for years and want something new and updated. We'd like to see something that is very eye-catching that sets us apart from your average run-of-the-mill business card.

We serve three communities with five locations in - Richmond, VA; Charlottesville, VA; and Durham, NC.

Industry/Entity Type

Burger Restaurant

Contact Information for Business Card

One side for a name, email, phone number and title but still POPS... The other side eye catching and unique.

Colors

Designer to choose colors to be used in the design.

Requirements
Nice to have
• We like these sayings:
• "A New Zealand Inspired Gastropub"
• "Life's a Cove"
• "All Green No Grain"
• "Life's Better at the Cove"
• "Intelligent Indulgence"
Should not have
• We are an upscale dine-in burger concept and not a typical dive bar or burger joint. We do not want to see "diner style" logos and designs.

```html
<!DOCTYPE html>
<html lang="en">
<head>
<meta charset="utf-8">
<title>Patty Cove Business Card</title>
<link rel="stylesheet" href="https://fonts.googleapis.com/css2?family=Josefin+Sans:wght@400;600;700&display=swap">
<style>
  :root {
    --canvas: #eeeeec;
    --card: #d8d9dc;
    --card-top: #e3e4e6;
    --ink: #1b1b1b;
    --band: #1c1c1c;
    --band-text: #f1f1f1;
    --rule: #9a9a9a;
  }
  * { margin: 0; padding: 0; box-sizing: border-box; }
  html, body { width: 1200px; height: 900px; overflow: hidden; background: var(--canvas); }
  .sheet {
    position: relative; width: 1200px; height: 900px;
    display: flex; flex-direction: column; align-items: center; justify-content: center; gap: 56px;
  }
  .card {
    position: relative; width: 620px; height: 354px; background: var(--card);
    box-shadow: 0 6px 18px rgba(0,0,0,0.15); overflow: hidden;
  }
  /* front */
  .card-front .masthead {
    position: absolute; top: 0; left: 0; right: 0; height: 150px; background: var(--card-top);
    display: flex; flex-direction: column; align-items: center; justify-content: flex-end; padding-bottom: 14px;
    font-family: "Josefin Sans", sans-serif; color: var(--ink);
  }
  .brand-name { font-size: 62px; font-weight: 700; letter-spacing: 5px; line-height: 1; text-transform: uppercase; }
  .brand-tagline { font-size: 17px; font-weight: 700; letter-spacing: 1.5px; margin-top: 4px; font-variant: small-caps; }
  .band-edge { position: absolute; left: 0; right: 0; top: 156px; height: 2px; background: var(--rule); }
  .contact-band {
    position: absolute; left: 0; right: 0; top: 162px; height: 148px; background: var(--band);
    color: var(--band-text); font-family: "Josefin Sans", sans-serif;
    display: flex; flex-direction: column; align-items: center; justify-content: center;
  }
  .phone { font-size: 30px; font-weight: 600; letter-spacing: 4px; }
  .divider { width: 430px; height: 1px; background: var(--band-text); margin: 12px 0 14px; opacity: 0.8; }
  .address { font-size: 15px; font-weight: 600; letter-spacing: 2px; text-transform: uppercase; }
  .email { font-size: 14px; letter-spacing: 1px; margin-top: 8px; opacity: 0.75; }
  /* back */
  .card-back { display: flex; align-items: center; justify-content: center; }
  .back-mark {
    display: flex; align-items: center; gap: 16px;
    font-family: "Josefin Sans", sans-serif; font-weight: 700; color: var(--ink);
  }
  .back-dot { width: 22px; height: 22px; border-radius: 50%; background: var(--ink); }
  .back-name { font-size: 34px; letter-spacing: 3px; text-transform: uppercase; line-height: 1; padding-top: 6px; }
</style>
</head>
<body>
<main class="sheet">
  <section class="card card-front" aria-label="Business card front">
    <header class="masthead">
      <h1 class="brand-name">Patty Cove</h1>
      <p class="brand-tagline">A New Zealand Inspired Gastro Pub</p>
    </header>
    <div class="band-edge"></div>
    <div class="contact-band">
      <p class="phone">804 - 555 - 0142</p>
      <div class="divider"></div>
      <p class="address">218 Fernbrook Way &nbsp;•&nbsp; Ashland, VA 23005</p>
      <p class="email">ashland@pattycove.com</p>
    </div>
  </section>

  <section class="card card-back" aria-label="Business card back">
    <div class="back-mark">
      <span class="back-dot"></span>
      <p class="back-name">Patty Cove</p>
    </div>
  </section>
</main>
</body>
</html>
```